VerdaTurf - 11" x 4" Door Hanger, full color both sides

We need a door hanger designed, 11" x 4", full color both sides, We are a lawn care company that provides lawn mowing, and other services to clients. This door hanger will be place on the 9 neighbors of our current clients. The ad needs to state that we provided lawn service to one of their neighbors today, and that we are in their neighborhood each week on that day. The door hanger will have 4 printings, substituting the day of Tuesday, Wednesday, Thursday, and Friday. All the art work and text will remain the same except the day of the week. For information about VerdaTurf, please visit our website www.verdaturf-example.net. The main emphasis of the message should be that we are their every week on that day, and the benefits to them of using our service (ie. quality time with their family, golf, sports, resting, etc., instead of mowing the lawn). At the bottom of the door hanger will be a coupon offering their tenth (10th) lawn service free, which is the same as a 10% discount.

I have uploaded a template files for the front and back of an 11 x 4 door hanger, The templates are pdf, jpeg, or eps files. The final product can be a pdf, jpeg, or eps file.

Target Market(s)

Neighbors of our existing clients

Industry/Entity Type

Lawn Care

Font styles to use
Serif

Requirements
Must have
• Professional design and art, Short conversational message that relays the following thoughts:
• 1. We mowed your neighbor's lawn today!
• 2. We are in your neighborhood every Tuesday!
• 3. Our lawn service is guaranteed.
• 4. Call to action - Call us today! 512-748-3091
• 5. Of course our contact info, name, phone number, website address.
• 6. Coupon at bottom for "10th lawn service Free!"
Nice to have
• Art work from our website is fine to use, That carries our theme throughout our campaign.
Should not have
• Very wordy. This is basically a billboard, Have very few seconds to grab their attention.

```html
<!DOCTYPE html>
<html lang="en">
<head>
<meta charset="utf-8">
<title>VerdaTurf Door Hanger</title>
<link rel="stylesheet" href="https://fonts.googleapis.com/css2?family=Noto+Serif:wght@400;700&family=Roboto+Condensed:wght@400&family=Jost:wght@600;700&display=swap">
<style>
  :root {
    --ink: #111111;
    --paper: #ffffff;
    --band: #000000;
    --coupon-bg: rgba(255,255,255,0.85);
    --haze: #f4f2ee;
    --guide-trim: #e0141e;
    --guide-bleed: #2a2f8f;
    --guide-safe: #1aa64a;
  }
  html, body {
    margin: 0;
    padding: 0;
    width: 1200px;
    height: 2880px;
    overflow: hidden;
    background: var(--paper);
  }
  .hanger {
    position: relative;
    width: 1200px;
    height: 2880px;
    overflow: hidden;
    color: var(--ink);
  }
  .hanger__photo {
    position: absolute;
    inset: 0 0 473px 0;
    background:
      radial-gradient(ellipse 520px 900px at 1120px 1250px, rgba(224,48,58,0.75), rgba(224,48,58,0) 70%),
      radial-gradient(ellipse 420px 500px at 900px 600px, rgba(230,90,95,0.45), rgba(230,90,95,0) 70%),
      radial-gradient(ellipse 700px 700px at 60px 2200px, rgba(94,143,34,0.9), rgba(94,143,34,0) 70%),
      radial-gradient(ellipse 500px 600px at 1150px 2150px, rgba(143,191,58,0.8), rgba(143,191,58,0) 70%),
      radial-gradient(ellipse 400px 700px at 40px 900px, rgba(143,191,58,0.6), rgba(143,191,58,0) 70%),
      linear-gradient(180deg, #e9ece4 0%, var(--haze) 40%, #e4e8da 100%);
  }
  .hanger__band {
    position: absolute;
    left: 0;
    top: 2407px;
    width: 1200px;
    height: 473px;
    background: var(--band);
  }
  .guides {
    position: absolute;
    inset: 0;
    pointer-events: none;
  }
  .text { position: absolute; margin: 0; white-space: nowrap; line-height: 1; font-weight: 400; }
  .brand-title {
    left: 0; width: 1200px; top: 838px;
    text-align: center;
    font-family: "Noto Serif", Georgia, serif;
    font-weight: 400;
    font-size: 112px;
  }
  .brand-rule {
    position: absolute; left: 153px; top: 968px; width: 894px; height: 4px;
    background: var(--ink);
  }
  .tagline {
    left: 0; width: 1200px; top: 984px;
    text-align: center;
    font-family: "Roboto Condensed", "Arial Narrow", sans-serif;
    font-size: 56px;
    line-height: 80px;
  }
  .message {
    left: 157px;
    font-family: "Roboto Condensed", "Arial Narrow", sans-serif;
    font-size: 102px;
    line-height: 116px;
  }
  .message--mowed { top: 1315px; }
  .message--weekly { top: 1631px; line-height: 110px; }
  .weekday {
    right: 147px; top: 1843px;
    font-family: "Roboto Condensed", "Arial Narrow", sans-serif;
    font-size: 150px;
  }
  .call-to-action {
    left: 0; width: 1200px; top: 2070px;
    text-align: center;
    font-family: "Roboto Condensed", "Arial Narrow", sans-serif;
    font-size: 80px;
  }
  .phone {
    left: 0; width: 1200px; top: 2180px;
    text-align: center;
    font-family: "Jost", "Futura", sans-serif;
    font-weight: 700;
    font-size: 124px;
    letter-spacing: 4px;
  }
  .coupon {
    position: absolute;
    left: 230px; top: 2320px;
    width: 740px; height: 70px;
    box-sizing: border-box;
    border: 4px dashed var(--ink);
    background: var(--coupon-bg);
    display: flex; align-items: center; justify-content: center;
    font-family: "Noto Serif", Georgia, serif;
    font-weight: 700;
    font-size: 44px;
    white-space: nowrap;
  }
  .band-name {
    left: 0; width: 1200px; top: 2425px;
    text-align: center;
    font-family: "Jost", "Futura", sans-serif;
    font-weight: 600;
    font-size: 150px;
    letter-spacing: 4px;
    color: var(--paper);
  }
  .band-rule {
    position: absolute; left: 163px; top: 2591px; width: 874px; height: 5px;
    background: var(--paper);
  }
  .website {
    left: 0; width: 1200px; top: 2622px;
    text-align: center;
    font-family: "Jost", "Futura", sans-serif;
    font-weight: 600;
    font-size: 70px;
    color: var(--paper);
  }
</style>
</head>
<body>
<main class="hanger">
  <div class="hanger__photo" role="img" aria-label="Soft-focus photo of a red lawn mower cutting green grass, washed to a pale tint"></div>
  <div class="hanger__band"></div>

  <svg class="guides" width="1200" height="2880" viewBox="0 0 1200 2880" aria-hidden="true">
    <g fill="none" stroke-width="4">
      <line x1="90" y1="0" x2="90" y2="2880" stroke="var(--guide-trim)"/>
      <line x1="1110" y1="0" x2="1110" y2="2880" stroke="var(--guide-trim)"/>
      <line x1="0" y1="73" x2="1200" y2="73" stroke="var(--guide-trim)"/>
      <line x1="0" y1="2783" x2="1200" y2="2783" stroke="var(--guide-trim)"/>
      <rect x="123" y="120" width="954" height="2647" rx="100" stroke="var(--guide-bleed)" stroke-width="5"/>
      <rect x="147" y="147" width="907" height="2593" rx="73" stroke="var(--guide-safe)" stroke-width="5"/>
      <circle cx="593" cy="523" r="183" stroke="var(--guide-safe)" stroke-width="5"/>
      <circle cx="593" cy="523" r="147" stroke="var(--guide-bleed)" stroke-width="8"/>
      <circle cx="593" cy="523" r="120" stroke="var(--guide-trim)" stroke-width="5"/>
      <line x1="774" y1="500" x2="1077" y2="500" stroke="var(--guide-safe)" stroke-width="5"/>
      <line x1="774" y1="546" x2="1077" y2="546" stroke="var(--guide-safe)" stroke-width="5"/>
      <line x1="740" y1="512" x2="1077" y2="512" stroke="var(--guide-bleed)" stroke-width="5"/>
    </g>
  </svg>

  <h1 class="text brand-title">VerdaTurf</h1>
  <div class="brand-rule"></div>
  <p class="text tagline">Our guaranteed lawn care<br>service and prices mow<br>down the competition!</p>

  <p class="text message message--mowed">We mowed your<br>neighbor's lawn today!</p>
  <p class="text message message--weekly">We are in your<br>neighborhood every</p>
  <p class="text weekday">Tuesday!</p>

  <p class="text call-to-action">Call us today!</p>
  <p class="text phone">512.748.3091</p>

  <div class="coupon">Coupon: 10th lawn service Free!</div>

  <p class="text band-name">VERDATURF</p>
  <div class="band-rule"></div>
  <p class="text website">www.verdaturf-example.net</p>
</main>
</body>
</html>
```